KU Curiosities

We need a web design for an ecommerce website that sells innovative gadgets. ***We are in the early stages of the business and don't have official products yet, they are being created. so we need to use placeholders and fake content, please email me with any questions regarding this.

The web page must look modern, fresh and simple and include-

• Logo
• My Account & View Cart link
• Menu - Home, Shop, The Latest, About Us, FAQ, Blog, Contact Us
• Promo bar at the top of the page like on: http://www.plumandwren.example/plwr/ (you can use placeholder text for now)
• Search Box
• Chatterpage, Chirpline, Vidstream, Clipboardly and Orbnet+ icons
• Slogan “Amaze your friends”
• Free shipping on orders over $50
• Banner section - for now you can highlight one of the fake products below, focus on free shipping on order over $50 or some kind of fake promotion
• New Arrivals section - highlight these fake products since we don't have products yet so you can use these products as place holders-
1. https://www.brisketbay.example/tech-gadgets/the-vorntap
2. https://www.brisketbay.example/tech-gadgets/lobelatch-earbud-securer
3. https://www.brisketbay.example/tech-gadgets/pestavo-headfoams
• credit card logos
• paytrellis.example seal - https://check.paytrellis.example/ptseal/images/secure90x72.gif

Example websites:
http://www.plumandwren.example/plwr/
https://www.brisketbay.example/
http://www.tinmantles.example/
https://sproutwell.example/
http://zevrodesk.example/
http://www.dallowsco.example/
http://www.vistaframe.example/

Requirements
Must have
• • Logo
• Search Box
• credit card logos

```html
<!DOCTYPE html>
<html lang="en">
<head>
<meta charset="utf-8">
<title>KU Curiosities</title>
<link rel="stylesheet" href="https://fonts.googleapis.com/css2?family=Roboto+Slab:wght@300;400;700&family=Bree+Serif&family=Arimo:wght@400;700&display=swap">
<style>
  :root {
    --charcoal: #454545;
    --white: #ffffff;
    --ink: #222222;
    --muted: #555555;
    --sky: #4fc3ee;
    --navy: #13285a;
    --panel: #e0e0e0;
    --panel-edge: #cccccc;
    --card-edge: #d6d6d6;
    --icon-grey: #8a8a8a;
  }
  * { box-sizing: border-box; margin: 0; padding: 0; }
  html, body { width: 1200px; height: 1000px; overflow: hidden; }
  body { background: var(--white); font-family: "Roboto Slab", Georgia, serif; color: var(--ink); position: relative; }

  .promo-bar { position: absolute; top: 0; left: 0; width: 1200px; height: 24px; background: var(--charcoal);
    color: var(--white); font-family: "Bree Serif", Georgia, serif; font-size: 14px; line-height: 24px; text-align: center; white-space: nowrap; overflow: hidden; }

  .site-header { position: absolute; top: 24px; left: 0; width: 1200px; height: 181px; }
  .account-links { position: absolute; left: 124px; top: 70px; font-family: "Bree Serif", Georgia, serif; font-size: 18px; color: var(--muted); display: flex; align-items: center; gap: 5px; white-space: nowrap; }
  .account-links a { color: var(--muted); text-decoration: none; }
  .brand { position: absolute; left: 430px; top: 0; width: 340px; height: 181px; display: flex; align-items: center; justify-content: center; }
  .brand-name { font-family: "Roboto Slab", Georgia, serif; font-weight: 700; font-size: 36px; line-height: 44px; color: var(--navy); white-space: nowrap; }
  .search-box { position: absolute; left: 923px; top: 80px; width: 157px; height: 27px; border: 1px solid #9a9a9a; border-radius: 8px;
    font-family: "Bree Serif", Georgia, serif; font-size: 13px; color: #aaa; padding-left: 8px; line-height: 25px; }
  .search-box svg { position: absolute; right: 6px; top: 3px; }

  .main-nav { position: absolute; top: 205px; left: 0; width: 1200px; height: 60px; background: var(--charcoal);
    display: flex; justify-content: center; gap: 47px; align-items: center; }
  .main-nav a { color: var(--white); text-decoration: none; font-weight: 300; font-size: 24px; line-height: 30px; white-space: nowrap; }
  .main-nav a.is-current { border-bottom: 2px solid var(--white); }

  .hero { position: absolute; top: 265px; left: 0; width: 1200px; height: 300px; overflow: hidden; }
  .hero-photo { position: absolute; inset: 0; background: linear-gradient(90deg, #b9c2cc 0%, #4b4f5a 30%, #6b5a48 50%, #3a3c44 62%, #d9a56e 90%, #e9b98a 100%); }
  .hero-panel { position: absolute; inset: 0; }
  .hero-title { position: absolute; right: 185px; top: 27px; font-family: "Arimo", Arial, sans-serif; font-weight: 700; font-size: 24px; color: var(--white); }
  .hero-copy { position: absolute; left: 716px; top: 82px; width: 292px; font-family: "Arimo", Arial, sans-serif; font-size: 18px; line-height: 24px; color: var(--white); text-align: right; }
  .hero-shop { position: absolute; left: 895px; top: 226px; width: 94px; height: 32px; border: 2px solid var(--sky); color: var(--sky);
    font-family: "Roboto Slab", Georgia, serif; font-size: 18px; line-height: 28px; text-align: center; text-decoration: none; }
  .hero-arrow { position: absolute; top: 128px; }

  .new-arrivals-title { position: absolute; left: 323px; top: 588px; font-size: 24px; font-weight: 400; line-height: 30px; }
  .product-card { position: absolute; top: 640px; width: 235px; height: 241px; border: 1px solid var(--card-edge); text-align: center; }
  .product-card .product-photo { margin: 2px auto 0; width: 229px; height: 171px; }
  .product-name { font-size: 18px; line-height: 24px; margin-top: 2px; }
  .product-shop { display: inline-block; margin-top: 8px; width: 84px; height: 28px; border: 2px solid var(--sky); color: var(--sky);
    font-size: 18px; font-weight: 300; line-height: 24px; text-decoration: none; }

  .shipping-promo { position: absolute; left: 843px; top: 643px; width: 235px; height: 241px; background: var(--panel); border: 1px solid var(--panel-edge); text-align: center; }
  .shipping-promo svg { margin-top: 32px; }
  .shipping-free { color: var(--sky); font-weight: 700; font-size: 28px; line-height: 30px; margin-top: 30px; }
  .shipping-text { font-size: 26px; line-height: 31px; }

  .site-footer { position: absolute; top: 900px; left: 0; width: 1200px; height: 100px; background: var(--charcoal); }
  .payment-methods { position: absolute; left: 120px; top: 29px; display: flex; gap: 4px; align-items: center; height: 42px; }
  .payment-method { height: 20px; padding: 0 3px; background: var(--white); color: var(--navy); font-size: 8px; line-height: 20px; white-space: nowrap; }
  .secure-seal { width: 42px; height: 42px; border-radius: 50%; background: #c9b36a; margin-left: 6px; }
  .copyright { position: absolute; left: 0; width: 1200px; top: 43px; text-align: center; color: var(--white); font-size: 13px; line-height: 16px; }
  .social-links { position: absolute; right: 118px; top: 39px; display: flex; gap: 4px; }
  .social-link { display: flex; flex-direction: column; align-items: center; color: var(--white); font-size: 7px; line-height: 9px; text-decoration: none; gap: 3px; width: 34px; white-space: nowrap; }
  .social-link .dot { width: 32px; height: 32px; border-radius: 50%; }
</style>
</head>
<body>
  <div class="promo-bar">Lorem ipsum dolor sit amet, consectetur adipisicing elit, sed do eiusmod tempor incididunt ut labore et dolore magna aliqua.&nbsp; ad</div>

  <header class="site-header">
    <div class="account-links">
      <a href="#">My account</a> |
      <svg width="20" height="16" viewBox="0 0 20 16" aria-hidden="true"><rect x="1" y="5" width="18" height="10" rx="2" fill="none" stroke="#555" stroke-width="2"/><path d="M6 5 V3 a2 2 0 0 1 2 -2 h4 a2 2 0 0 1 2 2 V5" fill="none" stroke="#555" stroke-width="2"/></svg>
      <a href="#">(0)</a>
    </div>
    <div class="brand">
      <div class="brand-name">KU Curiosities</div>
    </div>
    <div class="search-box">Search
      <svg width="20" height="20" viewBox="0 0 20 20" aria-hidden="true"><circle cx="8" cy="8" r="6" fill="none" stroke="#888" stroke-width="2"/><line x1="12.5" y1="12.5" x2="18" y2="18" stroke="#888" stroke-width="2.5"/></svg>
    </div>
  </header>

  <nav class="main-nav">
    <a href="#" class="is-current">Home</a>
    <a href="#">Shop</a>
    <a href="#">The Latest</a>
    <a href="#">About Us</a>
    <a href="#">FAQ</a>
    <a href="#">Blog</a>
    <a href="#">Contact Us</a>
  </nav>

  <section class="hero">
    <div class="hero-photo" role="img" aria-label="Close-up photo of a gadget with cables"></div>
    <svg class="hero-panel" width="1200" height="300" aria-hidden="true">
      <polygon points="728,0 1063,0 1012,300 676,300" fill="#0f1012" fill-opacity="0.85"/>
    </svg>
    <svg class="hero-arrow" style="left:118px" width="36" height="46" viewBox="0 0 36 46" aria-hidden="true"><polyline points="32,2 6,23 32,44" fill="none" stroke="#fff" stroke-opacity="0.75" stroke-width="5"/></svg>
    <svg class="hero-arrow" style="left:1046px" width="36" height="46" viewBox="0 0 36 46" aria-hidden="true"><polyline points="4,2 30,23 4,44" fill="none" stroke="#fff" stroke-opacity="0.75" stroke-width="5"/></svg>
    <h2 class="hero-title">Lorem ipsum</h2>
    <p class="hero-copy">Lorem ipsum dolor sit amet, con-sectetur adipisicing elit, sed do porro quisquam est, qui dolorem ipsum quia dolor sit amet, consec-tetur, adipisci velit, sed quia non</p>
    <a href="#" class="hero-shop">SHOP</a>
  </section>

  <h2 class="new-arrivals-title">NEW ARRIVALS</h2>

  <article class="product-card" style="left:117px">
    <div class="product-photo" role="img" aria-label="Product photo of four coloured hanging clip hooks on a rail" style="background:linear-gradient(90deg,#c8c8c8,#7c8ea8 40%,#a06a6a 65%,#5a5a5a)"></div>
    <div class="product-name">Lorem ipsum</div>
    <a href="#" class="product-shop">SHOP</a>
  </article>

  <article class="product-card" style="left:440px">
    <div class="product-photo" role="img" aria-label="Product photo of black earbud securers on white earbuds" style="background:radial-gradient(circle at 45% 50%,#2a2a2a 0%,#555 35%,#f4f4f4 70%)"></div>
    <div class="product-name">Lorem ipsum</div>
    <a href="#" class="product-shop">SHOP</a>
  </article>

  <aside class="shipping-promo">
    <svg width="110" height="50" viewBox="0 0 110 50" aria-hidden="true">
      <g fill="var(--icon-grey)">
        <rect x="0" y="10" width="30" height="2"/><rect x="6" y="20" width="26" height="2"/><rect x="4" y="30" width="28" height="2"/>
        <rect x="44" y="2" width="32" height="36" rx="3"/>
        <path d="M78 12 h14 l16 14 v12 h-30 z"/>
        <circle cx="58" cy="42" r="7" fill="var(--panel)"/><circle cx="58" cy="42" r="5"/>
        <circle cx="96" cy="42" r="7" fill="var(--panel)"/><circle cx="96" cy="42" r="5"/>
      </g>
    </svg>
    <div class="shipping-free">FREE</div>
    <div class="shipping-text">shipping on orders<br>over $50</div>
  </aside>

  <footer class="site-footer">
    <div class="payment-methods">
      <span class="payment-method">Paywisp</span>
      <span class="payment-method">Vantra</span>
      <span class="payment-method">Meridcard</span>
      <span class="payment-method">Dashpay</span>
      <span class="payment-method">Amberline</span>
      <div class="secure-seal" role="img" aria-label="Payment security seal"></div>
    </div>
    <p class="copyright">Copyright © 2014 KU Curiosities</p>
    <div class="social-links">
      <a href="#" class="social-link"><span class="dot" style="background:#3b5998"></span>Chatterpage</a>
      <a href="#" class="social-link"><span class="dot" style="background:#29a9e1"></span>Chirpline</a>
      <a href="#" class="social-link"><span class="dot" style="background:#e52d27"></span>Vidstream</a>
      <a href="#" class="social-link"><span class="dot" style="background:#cb2027"></span>Clipboardly</a>
      <a href="#" class="social-link"><span class="dot" style="background:#dd4b39"></span>Orbnet+</a>
    </div>
  </footer>
</body>
</html>
```